Need an enewsletter designed and built into mu MailChimp account

I need a new newsletter template. It should have room for a banner image up top and four articles and allow me to embed video, if I so choose. We will need to be able to content manage this in mailchimp. Take branding from our website cobaltnestlab.com

Focus on the black and red and white colours per the website.
After a slick look and feel that will easily accommodate and complement images from our apps. See here: https://cobaltnestlab.com/

Target Market(s)

Professionals at corporate level in the residential property development industry

Font styles to use
Sans Serif

Colors
f04a50
ffffff

Requirements
Must have
• Logo
web address cobaltnestlab.com
Responsive
High tech/slick Pellor-type look per website

```html
<!DOCTYPE html>
<html lang="en">
<head>
<meta charset="utf-8">
<title>Cobaltnest CRM Newsletter</title>
<link rel="stylesheet" href="https://fonts.googleapis.com/css2?family=Poppins:wght@400;500;600;700&family=Roboto+Condensed:wght@700&display=swap">
<style>
  :root {
    --navy: #36335a;
    --ink: #1c1c1c;
    --body: #222;
    --muted: #7a7a7a;
    --hero-bg: #f3f3f5;
    --soft-bg: #f9f9f9;
    --col-left: #f4f4f4;
    --col-right: #dedede;
    --accent: #fd8a6f;
    --brand-red: #f04a50;
    --white: #ffffff;
    --social: #6a6a6a;
  }
  * { margin: 0; padding: 0; box-sizing: border-box; }
  html, body { width: 1200px; height: 4500px; overflow: hidden; }
  body { font-family: "Poppins", sans-serif; color: var(--body); background: var(--white); }
  .headline { font-family: "Roboto Condensed", sans-serif; font-weight: 700; color: var(--ink); }

  .browser-bar { height: 73px; background: var(--navy); color: var(--white); font-size: 21px; display: flex; align-items: center; justify-content: center; }

  .masthead { height: 173px; display: flex; align-items: center; justify-content: space-between; padding: 0 162px 0 161px; }
  .brand { display: flex; align-items: center; gap: 14px; font-weight: 700; font-size: 42px; color: var(--ink); }
  .brand-mark { width: 22px; height: 22px; background: var(--brand-red); }
  .tagline { font-weight: 600; font-size: 30px; line-height: 36px; color: #555; }
  .tagline span { display: block; padding-left: 36px; }

  .hero { height: 1008px; background: var(--hero-bg); text-align: center; position: relative; }
  .hero-screen { position: absolute; left: 200px; top: 86px; width: 848px; height: 472px; border-radius: 18px 18px 6px 6px;
    background: linear-gradient(180deg, #3b3f44 0%, #5a6470 10%, #eef1f5 12%, #dfe5ec 60%, #7f8a95 100%); }
  .hero h1 { position: absolute; top: 600px; width: 100%; font-size: 70px; }
  .hero p { position: absolute; top: 740px; left: 150px; width: 900px; font-size: 22px; line-height: 36px; }
  .cta { position: absolute; left: 442px; top: 874px; width: 314px; height: 75px; background: var(--accent); color: var(--white);
    font-weight: 600; font-size: 22px; letter-spacing: 1.5px; display: flex; align-items: center; justify-content: center; text-decoration: none; }

  .article { background: var(--soft-bg); text-align: center; padding: 68px 180px 0; }
  .article h2 { font-size: 46px; line-height: 56px; margin-bottom: 46px; }
  .article p { color: var(--muted); font-size: 22px; line-height: 36px; margin-bottom: 36px; }
  .article-one { height: 547px; }
  .article-four { height: 624px; padding-top: 84px; }

  .split { display: flex; height: 707px; }
  .split-col { width: 50%; padding: 68px 20px 0 166px; }
  .split-right { padding: 68px 150px 0 38px; }
  .split-left { background: var(--col-left); }
  .split-right { background: var(--col-right); }
  .split-col h2 { font-size: 44px; line-height: 56px; margin-bottom: 34px; white-space: nowrap; letter-spacing: -0.3px; }
  .split-col p { color: var(--muted); font-size: 22px; line-height: 36px; margin-bottom: 36px; }
  .split-left p { padding-right: 20px; }

  .video { height: 763px; text-align: center; position: relative; }
  .video h2 { font-size: 46px; padding-top: 68px; }
  .video-frame { position: absolute; left: 112px; top: 190px; width: 974px; height: 507px;
    background: radial-gradient(ellipse at 50% 55%, #5c4a3a 0%, #2c2a30 45%, #1a1a1f 100%); border: 14px solid #2b2a3c; }
  .play { position: absolute; left: 599px; top: 435px; transform: translate(-50%, -50%); }

  .footer { height: 362px; background: var(--navy); color: var(--white); position: relative; }
  .footer-brand { position: absolute; left: 268px; top: 100px; font-weight: 700; font-size: 42px; color: var(--white); }
  .footer-tag { position: absolute; left: 268px; top: 205px; font-weight: 600; font-size: 30px; line-height: 36px; color: var(--white); }
  .footer-tag span { display: block; padding-left: 36px; }
  .contact { position: absolute; left: 617px; top: 64px; font-size: 22px; line-height: 45px; }
  .contact b { font-weight: 600; color: #d8d7e3; letter-spacing: 0.5px; }
  .branches { position: absolute; left: 614px; top: 218px; font-size: 21px; line-height: 36px; }
  .branches b { font-weight: 600; color: #d8d7e3; font-size: 22px; display: block; margin-bottom: 2px; }

  .social { height: 243px; display: flex; justify-content: center; gap: 9px; padding-top: 80px; }
  .social a { width: 74px; height: 74px; border-radius: 50%; background: var(--social); display: block; }
</style>
</head>
<body>
  <div class="browser-bar">View in web browser</div>

  <header class="masthead">
    <div class="brand"><span class="brand-mark"></span>Cobaltnest</div>
    <div class="tagline">Building<span>since 2004</span></div>
  </header>

  <section class="hero">
    <div class="hero-screen" role="img" aria-label="Laptop showing the Cobaltnest CRM app with a grid of house listings"></div>
    <h1 class="headline">Cobaltnest CRM</h1>
    <p>Quisque sagittis orci est, eget laoreet dolor hendrerit non. Vestibulum consequat elementum porta. Pellentesque aliquam posuere ullamcorper. Aliquam quis gravida nisi, sit amet rhoncus lorem.</p>
    <a class="cta" href="https://cobaltnestlab.com/">GET STARTED NOW</a>
  </section>

  <section class="article article-one">
    <h2 class="headline">Lorem Ipsum Dolor Sit</h2>
    <p>Duis iaculis dui eget odio suscipit, in porta diam gravida. Sed rutrum maximus dictum. Aliquam quam neque, vulputate a tellus vel, lobortis blandit ante. Phasellus sit amet ornare mauris, cursus imperdiet augue.</p>
    <p>Nulla ac tortor vitae nulla porttitor convallis et at sapien. Maecenas et pulvinar velit, quis maximus metus. Etiam sed erat purus. Duis iaculis dui eget odio suscipit, in porta diam gravida. Sed rutrum maximus dictum. Aliquam quam neque, vulputate a tellus vel, lobortis blandit ante.</p>
  </section>

  <section class="split">
    <article class="split-col split-left">
      <h2 class="headline">Lorem Ipsum Dolor Sit</h2>
      <p>Duis iaculis dui eget odio suscipit, in porta diam gravida. Sed rutrum maximus dictum. Aliquam quam neque, vulputate a tellus vel, lobortis blandit ante. Phasellus sit amet ornare mauris, cursus imperdiet augue.</p>
      <p>Nulla ac tortor vitae nulla porttitor convallis et at sapien. Maecenas et pulvinar velit, quis maximus metus. Etiam sed erat purus.</p>
    </article>
    <article class="split-col split-right">
      <h2 class="headline">Nulla Ac Tortor Vitae</h2>
      <p>Duis iaculis dui eget odio suscipit, in porta diam gravida. Sed rutrum maximus dictum. Aliquam quam neque, vulputate a tellus vel, lobortis blandit ante. Phasellus sit amet ornare mauris, cursus imperdiet augue.</p>
      <p>Nulla ac tortor vitae nulla porttitor convallis et at sapien. Maecenas et pulvinar velit, quis maximus metus. Etiam sed erat purus.</p>
    </article>
  </section>

  <section class="article article-four">
    <h2 class="headline">Donec Sit Amet Orci Vestibulam</h2>
    <p>Donec sit amet orci vestibulum, efficitur urna nec, eleifend nisl. Quisque ultrices magna sit amet mi interdum dignissim. Donec egestas dapibus augue nec hendrerit. Morbi vitae maximus felis, at auctor tortor. Pellentesque vulputate erat tortor, id convallis arcu interdum eget.</p>
    <p>Nulla egestas varius metus id ultrices. Phasellus quis nisi vestibulum, dignissim lorem ut, dignissim sapien. Curabitur tempor malesuada diam, quis ultrices est varius quis. Nunc eget dolor nec dolor lobortis pulvinar in viverra elit. Nunc eu lobortis leo, in congue orci.</p>
  </section>

  <section class="video">
    <h2 class="headline">Play The Video</h2>
    <div class="video-frame" role="img" aria-label="Video still of the Cobaltnest dashboards on a laptop in a dark setting"></div>
    <svg class="play" width="104" height="104" viewBox="0 0 104 104" aria-label="Play video">
      <circle cx="52" cy="52" r="52" fill="#f4846c"/>
      <path d="M42 34 L72 52 L42 70 Z" fill="#ffffff"/>
    </svg>
  </section>

  <footer class="footer">
    <div class="footer-brand">Cobaltnest</div>
    <div class="footer-tag">Building<span>since 2004</span></div>
    <div class="contact">
      <div><b>Phone:</b> 8888 .555.0142</div>
      <div><b>Email:</b> sales@cobaltnestlab.com</div>
      <div><b>Website:</b> www.cobaltnestlab.com</div>
    </div>
    <div class="branches">
      <b>Branches</b>
      <div>Hobart, Australia</div>
      <div>Austin, USA, Pune, India</div>
    </div>
  </footer>

  <nav class="social" aria-label="Social links">
    <a href="#" aria-label="Professional network"></a>
    <a href="#" aria-label="Social page"></a>
    <a href="#" aria-label="Video channel"></a>
  </nav>
</body>
</html>
```